Marketing Expert Needs a Book Cover Design to Inspire Audiences

Need a book cover design for my first book!
The book is a ‘How To’ serious non fiction book. It has insights for marketers on how to transform their marketing to help their organizations accelerate sales and drive growth. This is not a high level theoretical book about brand building. Instead this includes strategic frameworks, and tried and tested ideas and tactics which marketers (or aspiring marketers) can use to be successful in their jobs. The premise of this book is that it’s no longer enough for marketers to focus on brand recognition. We need to help the business to create demand and make it easier for our sales colleagues to close deals.
The aim is to inspire readers with insights so that they think differently about themselves and their marketing. The aim is to compel them to take start new conversations to accelerate sales, using the tools, concepts and case studies outlined in the book.
The Title: The Growth Signal
Subtitle: Steps to Win Buyers by Storytelling, Curiosity and Trusted Voices.
The cover must have a compelling visual which communicates this idea-
The Growth Signal Inspires You to Think Different so That You Scale/Overcome the Limits you might have placed on yourself or your business.
I like a simple and clean look. I'm attaching some samples which I like. Looking to achieve the same look for my book cover.
Update- I need the cover for an ebook only. Since the cover will be displayed as a thumbnail in Verbolt and other online shopping sites, it should be without any clutter with good contrast between images and text. This will help with visibility.
Updates
Key Art Style designs will also be welcome. Added Saturday, September 24, 2016
Reason: I'm hoping that atleast some more top 20 designers will respond.
Target Market(s)
Target market is CMOs, Marketing Managers, Business Leaders, MBA students- anyone who is looking to reshape and rejig their marketing skills and teams.
Industry/Entity Type
Marketing
Requirements
Must have
- A compelling visual is a must have.
- It shouldn't have only text.
Nice to have
- Please refer the cover samples I sent.
- Key Art designs will also be welcome.
Should not have
- Clutter.
- I like simplicity.

```html
<!DOCTYPE html>
<html lang="en">
<head>
<meta charset="utf-8">
<title>The Growth Signal — Book Cover</title>
<link href="https://fonts.googleapis.com/css2?family=Noto+Serif:ital,wght@0,500;0,600;1,400;1,500&display=swap" rel="stylesheet">
<style>
  :root {
    --stage: #ececec;
    --paper: #fafafa;
    --signal-yellow: #f4e41c;
    --ink-blue: #1d4b98;
    --frame-blue: #b3c6ea;
    --beam-blue: #a9bfe8;
    --photo-yellow: #e9e13a;
    --photo-blue: #3556a3;
  }
  html, body {
    margin: 0;
    width: 1200px;
    height: 970px;
    overflow: hidden;
    background: var(--stage);
  }
  .cover {
    position: absolute;
    left: 300px;
    top: 30px;
    width: 600px;
    height: 910px;
    background: var(--paper);
    overflow: hidden;
    box-shadow: 0 6px 24px rgba(0,0,0,0.12);
    font-family: "Noto Serif", Georgia, serif;
  }
  .cover-shapes {
    position: absolute;
    inset: 0;
  }
  .cover-photo {
    position: absolute;
    left: 75px;
    top: 440px;
    width: 430px;
    height: 370px;
    background: linear-gradient(160deg, var(--photo-yellow) 0%, #c9cf5a 35%, var(--photo-blue) 75%, #2b4a96 100%);
  }
  .focus-circle {
    position: absolute;
    left: 0;
    top: 0;
  }
  .title-article,
  .title-main,
  .title-sub {
    position: absolute;
    margin: 0;
    line-height: 1;
    white-space: nowrap;
  }
  .title-article {
    left: 150px;
    top: 62px;
    font-style: italic;
    font-weight: 500;
    font-size: 60px;
    color: var(--ink-blue);
  }
  .title-main {
    left: 0;
    right: 0;
    top: 150px;
    text-align: center;
    font-weight: 500;
    font-size: 128px;
    letter-spacing: -3px;
    color: var(--signal-yellow);
    mix-blend-mode: multiply;
  }
  .title-sub {
    left: 0;
    right: 0;
    top: 305px;
    text-align: center;
    font-style: italic;
    font-weight: 500;
    font-size: 118px;
    letter-spacing: -1px;
    color: var(--ink-blue);
  }
  .subtitle {
    position: absolute;
    left: 0;
    right: 0;
    top: 838px;
    margin: 0;
    text-align: center;
    font-style: italic;
    font-weight: 400;
    font-size: 19px;
    line-height: 1.25;
    color: var(--ink-blue);
  }
</style>
</head>
<body>
  <main class="cover">
    <svg class="cover-shapes" width="600" height="910" viewBox="0 0 600 910" aria-hidden="true">
      <defs>
        <linearGradient id="beam-fade" x1="0" y1="0" x2="0" y2="1">
          <stop offset="0" stop-color="var(--beam-blue)" stop-opacity="0.9"/>
          <stop offset="0.6" stop-color="var(--beam-blue)" stop-opacity="0.55"/>
          <stop offset="1" stop-color="var(--beam-blue)" stop-opacity="0.15"/>
        </linearGradient>
      </defs>
      <polygon class="light-beam" points="215,0 400,0 305,395" fill="url(#beam-fade)"/>
      <rect class="cover-frame" x="70" y="90" width="470" height="725" fill="none" stroke="var(--frame-blue)" stroke-width="10"/>
    </svg>

    <div class="cover-photo" role="img" aria-label="Duotone yellow and blue photograph of a person in profile, head tilted back, gazing upward"></div>

    <svg class="focus-circle" width="600" height="910" viewBox="0 0 600 910" aria-hidden="true">
      <circle cx="305" cy="510" r="73" fill="#4e6a8c" fill-opacity="0.4"/>
    </svg>

    <h1 class="book-title">
      <span class="title-article">The</span>
      <span class="title-main">GROWTH</span>
      <span class="title-sub">Signal</span>
    </h1>

    <p class="subtitle">Steps to Win Buyers by Storytelling,<br>Curiosity and Trusted Voices.</p>
  </main>
</body>
</html>
```